Velvet Lantern rebranding my business with a new business card

I have my new logo and now I need a refresher on my business cards. I really want something fun and fresh. I like black background or anything to make the color pop.
Logo
Name: Velvet Lantern
Contact Info as stated below:
Mara Pelkin
519-555-0147
Logo
Name: Velvet Lantern
Mara Pelkin
519-555-0147
fb.me/VelvetLanternbyMara
Instagram: @VelvetLanternbyMara

Industry/Entity Type

Business

Contact Information for Business Card

double-sided. Logo on one side. Contact info on the other.

Requirements
Must have
• Logo
• Name: Velvet Lantern
• Contact Info as stated below:
• Mara Pelkin
• 519-555-0147
• fb.me/VelvetLanternbyMara
• fb.me/VelvetLanternbyMara

```html
<!DOCTYPE html>
<html lang="en">
<head>
<meta charset="utf-8">
<title>Velvet Lantern — Business Cards</title>
<link rel="stylesheet" href="https://fonts.googleapis.com/css2?family=Montserrat:wght@400;500&display=swap">
<style>
  :root {
    --backdrop: #c9c9cb;
    --card: #0d0b0d;
    --card-edge: #1c181b;
    --icing: #e9a6c5;
    --icing-deep: #c97ba0;
    --ring: #e8a0c0;
    --ink-light: #ffffff;
    --ink-dark: #2a1f25;
  }
  * { box-sizing: border-box; margin: 0; padding: 0; }
  html, body {
    width: 1200px;
    height: 973px;
    overflow: hidden;
    background: var(--backdrop);
    font-family: "Montserrat", sans-serif;
  }
  .canvas { position: relative; width: 1200px; height: 973px; }

  .card {
    position: absolute;
    width: 533px;
    height: 305px;
    background: var(--card);
    border-radius: 10px;
    overflow: hidden;
    box-shadow: 0 0 0 1px var(--card-edge);
  }
  .card--front { left: 135px; top: 13px; }
  .card--logo-back { left: 292px; top: 332px; }
  .card--alt-back { left: 135px; top: 655px; }

  .icing-band {
    position: absolute;
    left: 0; top: 0;
    width: 100%;
    height: 78px;
    background: linear-gradient(180deg, var(--icing) 0%, var(--icing) 55%, var(--icing-deep) 100%);
  }

  .front-info {
    position: absolute;
    left: 0; right: 0;
    text-align: center;
    color: var(--ink-light);
  }
  .business-name {
    top: 90px;
    font-size: 27px;
    font-weight: 500;
    color: var(--icing);
    letter-spacing: 1px;
  }
  .role {
    top: 127px;
    font-size: 13px;
    font-weight: 400;
  }
  .contact-block { top: 175px; font-size: 25px; font-weight: 400; line-height: 34px; }

  .social-pill {
    position: absolute;
    left: 135px;
    top: 268px;
    width: 311px;
    height: 19px;
    border-radius: 10px;
    background: var(--icing);
    display: flex;
    align-items: center;
    justify-content: center;
    gap: 6px;
    font-size: 8.5px;
    color: var(--ink-dark);
    white-space: nowrap;
  }
  .social-dot {
    width: 11px; height: 11px;
    border-radius: 50%;
    background: var(--ink-dark);
  }

  .logo-ring {
    position: absolute;
    border: 3px solid var(--ring);
    border-radius: 50%;
    display: flex;
    align-items: center;
    justify-content: center;
    text-align: center;
    background: var(--card);
  }
  .logo-ring--large { width: 292px; height: 292px; left: 120px; top: 6px; }
  .logo-ring--small { width: 124px; height: 124px; left: 204px; top: 102px; }
  .logo-word {
    color: var(--icing);
    font-weight: 500;
    letter-spacing: 1px;
    line-height: 1.2;
  }
  .logo-ring--large .logo-word { font-size: 30px; }
  .logo-ring--small .logo-word { font-size: 15px; }
</style>
</head>
<body>
<main class="canvas">

  <section class="card card--front" aria-label="Business card front, contact details">
    <div class="icing-band" role="img" aria-label="Pink dripping icing border"></div>
    <p class="front-info business-name">Velvet Lantern</p>
    <p class="front-info role">Owner/Creator</p>
    <div class="front-info contact-block">
      <p class="contact-name">Mara Pelkin</p>
      <p class="contact-phone">519-555-0147</p>
    </div>
    <div class="social-pill">
      <span class="social-handle">@VelvetLanternbyMara</span>
      <span class="social-dot" aria-hidden="true"></span>
      <span class="social-dot" aria-hidden="true"></span>
      <span class="social-link">fb.me/VelvetLanternbyMara</span>
    </div>
  </section>

  <section class="card card--logo-back" aria-label="Business card back, logo">
    <div class="logo-ring logo-ring--large">
      <p class="logo-word">Velvet<br>Lantern</p>
    </div>
  </section>

  <section class="card card--alt-back" aria-label="Business card back, alternate with icing border">
    <div class="icing-band" role="img" aria-label="Pink dripping icing border"></div>
    <div class="logo-ring logo-ring--small">
      <p class="logo-word">Velvet<br>Lantern</p>
    </div>
  </section>

</main>
</body>
</html>
```